Bright Tooth Dentistry Business Card

We need business cards for our dental office.
We are looking for a clean, elegant design

We provide dental services to children.
Our card needs to be appealing to referring dentists, parents and our team

Target Market(s)

referring dentists, parents and our team

Industry/Entity Type

Dental Clinic

Contact Information for Business Card

4816 Juniper Lane, Suite 100
Cedar Hollow, PA 15237

412-837-2961 Voice
412-837-2962 fax
info@brighttoothdentalpa.com email
www.brighttoothdentalpa.com web

Font styles to use
Sans Serif

Requirements
Must have
• White background - clean, crisp, elegant, simple
• rounded corners
• different color palate - once we come up with design, we will replace the blue with orange, green,
Nice to have
• Follow our logo typeface and colors
• then we can replace color

```html
<!DOCTYPE html>
<html lang="en">
<head>
<meta charset="utf-8">
<title>Bright Tooth Dentistry – Business Card</title>
<link href="https://fonts.googleapis.com/css2?family=Poppins:wght@400;500;600&display=swap" rel="stylesheet">
<style>
  :root {
    --brand-blue: #08a3e6;
    --brand-grey: #a7a9ac;
    --card-white: #ffffff;
    --stage: #eceff2;
    --ink-white: #ffffff;
  }
  * { margin: 0; padding: 0; box-sizing: border-box; }
  html, body {
    width: 1200px;
    height: 900px;
    overflow: hidden;
    background: var(--stage);
    font-family: "Poppins", sans-serif;
  }
  .sheet {
    width: 1200px;
    height: 900px;
    display: flex;
    align-items: center;
    justify-content: center;
    gap: 40px;
  }
  .card {
    position: relative;
    width: 540px;
    height: 309px;
    border-radius: 24px;
    overflow: hidden;
    background: var(--card-white);
    box-shadow: 0 6px 20px rgba(0, 0, 0, 0.12);
  }
  .card-shape {
    position: absolute;
    inset: 0;
    width: 100%;
    height: 100%;
  }
  .shape-blue { fill: var(--brand-blue); }
  .shape-white { fill: var(--card-white); }

  /* front */
  .brand-lockup {
    position: absolute;
    left: 110px;
    top: 96px;
    display: flex;
    align-items: center;
    gap: 14px;
  }
  .brand-dot {
    width: 26px;
    height: 26px;
    border-radius: 50%;
    background: var(--brand-blue);
    flex: none;
  }
  .brand-name {
    font-size: 34px;
    font-weight: 500;
    color: var(--brand-blue);
    letter-spacing: -0.5px;
    line-height: 1.1;
  }

  /* back */
  .contact {
    position: absolute;
    right: 34px;
    top: 30px;
    text-align: right;
    color: var(--ink-white);
  }
  .contact-name {
    font-size: 26px;
    font-weight: 600;
    letter-spacing: -0.3px;
    margin-bottom: 10px;
  }
  .contact-line {
    font-size: 11.5px;
    font-weight: 400;
    line-height: 1.55;
  }
  .contact-web {
    font-size: 13px;
    font-weight: 600;
    margin: 4px 0 8px;
  }
</style>
</head>
<body>
<main class="sheet">
  <section class="card card-front" aria-label="Card front">
    <svg class="card-shape" viewBox="0 0 540 309" preserveAspectRatio="none" aria-hidden="true">
      <rect class="shape-blue" width="540" height="309"/>
      <ellipse class="shape-white" cx="350" cy="70" rx="370" ry="205"/>
    </svg>
    <div class="brand-lockup">
      <span class="brand-dot"></span>
      <span class="brand-name">Bright Tooth<br>Dentistry</span>
    </div>
  </section>

  <section class="card card-back" aria-label="Card back">
    <svg class="card-shape" viewBox="0 0 540 309" preserveAspectRatio="none" aria-hidden="true">
      <rect class="shape-blue" width="540" height="309"/>
      <ellipse class="shape-white" cx="40" cy="330" rx="330" ry="170"/>
    </svg>
    <div class="contact">
      <p class="contact-name">Bright Tooth Dentistry</p>
      <p class="contact-line">info@brighttoothdentalpa.com</p>
      <p class="contact-line">Ph: 412-837-2961 &nbsp;|&nbsp; Fax: 412-837-2962</p>
      <p class="contact-web">www.brighttoothdentalpa.com</p>
      <p class="contact-line">4816 Juniper Lane</p>
      <p class="contact-line">Suite 100, Cedar Hollow</p>
      <p class="contact-line">PA 15237</p>
    </div>
  </section>
</main>
</body>
</html>
```